Tall Gum Equipment Hire Business Card Design

Tall Gum Equipment Hire Pty Ltd

WET or DRY HIRE

Kestrel M5-8 + attachments
Turf Cutter
Lawn mowers with catchers
Brushcutters
Blowers

We require a business card with the above information for a new equipment hire Company. Would like to see a redish/brown background or something to do with an Australian Red Dog (Cattle Dog) on the business card as our Logo - even some sort of watermark as a background.

Industry/Entity Type

Business

Contact Information for Business Card

ABN: 81 207 935 316
17B Moller Road Emerald Qld 4720
PO Box 8157 Emerald Qld 4720
PH: 0413072846 or 0437150928
Email: sunvale.turf@quollnet.example

```html
<!DOCTYPE html>
<html lang="en">
<head>
<meta charset="utf-8">
<title>Tall Gum Equipment Hire – Business Card</title>
<link rel="stylesheet" href="https://fonts.googleapis.com/css2?family=Arimo:wght@400;700&display=swap">
<style>
  :root {
    --rust: #c63d17;
    --ink: #000000;
    --paper: #ffffff;
    --text-light: #ffffff;
  }
  * { margin: 0; padding: 0; box-sizing: border-box; }
  html, body {
    width: 1200px; height: 726px; overflow: hidden;
    background: var(--paper);
  }
  .card {
    position: relative;
    width: 1200px; height: 726px;
    background: var(--ink);
    border: 4px solid var(--ink);
    font-family: "Arimo", Arial, Helvetica, sans-serif;
    overflow: hidden;
  }
  .brand-panel {
    position: absolute; left: 0; top: 0;
    width: 542px; height: 718px;
    background: var(--paper);
    color: var(--ink);
    text-align: center;
  }
  .accent-stripe {
    position: absolute; left: 542px; top: 0;
    width: 37px; height: 718px;
    background: var(--rust);
  }
  .brand-mark {
    position: absolute; left: 211px; top: 190px;
    width: 120px; height: 120px;
    background: var(--rust);
  }
  .brand-name {
    position: absolute; left: 0; width: 542px; top: 408px;
    font-size: 72px; font-weight: 700; color: var(--rust);
    letter-spacing: 2px; line-height: 1;
  }
  .brand-tagline {
    position: absolute; left: 0; width: 542px; top: 497px;
    font-size: 40px; font-weight: 400; letter-spacing: 2px; line-height: 1;
  }
  .brand-entity {
    position: absolute; left: 0; width: 542px; top: 553px;
    font-size: 27px; line-height: 1;
  }
  .brand-abn {
    position: absolute; left: 0; width: 542px; top: 622px;
    font-size: 24px; line-height: 1;
  }
  .details {
    position: absolute; left: 632px; top: 0;
    color: var(--text-light);
    font-size: 29px; line-height: 1;
  }
  .hire-type {
    position: absolute; top: 93px; white-space: nowrap;
    font-weight: 400;
  }
  .hire-type strong { color: var(--rust); font-weight: 700; }
  .equipment-list { list-style: none; position: absolute; top: 153px; white-space: nowrap; }
  .equipment-list li {
    position: relative; height: 46.5px; padding-left: 34px;
  }
  .equipment-list li::before {
    content: ""; position: absolute; left: 2px; top: 5px;
    width: 18px; height: 18px; border-radius: 50%;
    background: var(--rust);
  }
  .contact { position: absolute; top: 465px; white-space: nowrap; }
  .contact p { height: 40px; }
  .contact .value { color: var(--rust); font-weight: 700; }
  .address { position: absolute; top: 581px; white-space: nowrap; }
  .address p { height: 40px; }
</style>
</head>
<body>
  <div class="card">
    <section class="brand-panel">
      <div class="brand-mark" aria-hidden="true"></div>
      <div class="brand-name">TALL GUM</div>
      <div class="brand-tagline">EQUIPMENT HIRE</div>
      <div class="brand-entity">PTY LTD</div>
      <div class="brand-abn">ABN 81 207 935 316</div>
    </section>
    <div class="accent-stripe"></div>
    <section class="details">
      <div class="hire-type"><strong>WET</strong> or <strong>DRY HIRE</strong></div>
      <ul class="equipment-list">
        <li>Kestrel M5-8 + attachments</li>
        <li>Turf Cutter</li>
        <li>Lawn mowers with catchers</li>
        <li>Brushcutters</li>
        <li>Blowers</li>
      </ul>
      <div class="contact">
        <p>Ph <span class="value">0413 072846</span> or <span class="value">0437 150928</span></p>
        <p>Email <span class="value">sunvale.turf@quollnet.example</span></p>
      </div>
      <div class="address">
        <p>17B Moller Road Emerald Qld 4720</p>
        <p>PO Box 8157 Emerald Qld 4720</p>
      </div>
    </section>
  </div>
</body>
</html>
```